Tessel PR (young, fun PR agency) needs a Business Card Design

We need a new business card design that reflects who we are as a company. We're a Sydney-based PR agency that's six years old with clients including Blue Heron, Duneprint, OLVEN, Lou Carvell etc. - just check out our website for more info: www.tesselpr.com.au. We would like to see designs that bring to life our company name and what we do (generating media coverage for brands on TV, radio, online and in newspapers and magazines). We don't want a corporate style card but one that people take notice of and think 'wow that's a cool business card'. It doesn't have to be the standard rectangle shape and can incorporate humour.

Target Market(s)

Clients (generally cool/creative types) and media

Industry/Entity Type

Business

Requirements
Must have
• The card must feature our business logo (which can be updated if you like) and use both sides.
Nice to have
• The card could feature a cool illustration

```html
<!DOCTYPE html>
<html lang="en">
<head>
<meta charset="utf-8">
<title>Tessel PR – Business Card</title>
<link rel="stylesheet" href="https://fonts.googleapis.com/css2?family=Saira+Condensed:wght@600;700&family=Arimo:wght@400&display=swap">
<style>
  :root {
    --backdrop: #ece8e1;
    --card-orange: #de9400;
    --band-orange: #f9a235;
    --ink: #111111;
    --strip-dark: #1c1c1c;
    --strip-mid: #3a3a3a;
    --paper-white: #ffffff;
    --card-shadow: rgba(0, 0, 0, 0.22);
  }
  * { margin: 0; padding: 0; box-sizing: border-box; }
  html, body {
    width: 1200px;
    height: 900px;
    overflow: hidden;
    background: var(--backdrop);
  }
  .canvas {
    position: relative;
    width: 1200px;
    height: 900px;
  }
  .card {
    position: absolute;
    width: 610px;
    height: 380px;
    background: var(--card-orange);
    overflow: hidden;
    box-shadow: 0 8px 22px var(--card-shadow);
  }
  .card--front { left: 130px; top: 50px; }
  .card--back { left: 450px; top: 470px; }

  .footer-strip {
    position: absolute;
    left: 0;
    right: 0;
    bottom: 0;
    height: 50px;
    background: linear-gradient(180deg, var(--strip-mid), var(--strip-dark));
  }
  .target-ring {
    position: absolute;
    width: 150px;
    height: 150px;
  }
  .card--front .target-ring { left: 440px; top: 80px; }
  .card--back .target-ring { left: 440px; top: 140px; }

  /* Front */
  .brand-name {
    position: absolute;
    left: 30px;
    top: 100px;
    font-family: "Saira Condensed", "Arial Narrow", sans-serif;
    font-weight: 700;
    font-size: 84px;
    line-height: 1;
    letter-spacing: 4px;
    color: var(--ink);
    text-transform: uppercase;
    white-space: nowrap;
  }
  .tagline-band {
    position: absolute;
    left: 20px;
    top: 212px;
    width: 440px;
    height: 44px;
    background: var(--band-orange);
  }
  .tagline {
    position: absolute;
    left: 12px;
    top: 8px;
    font-family: "Saira Condensed", "Arial Narrow", sans-serif;
    font-weight: 700;
    font-size: 25px;
    line-height: 1.1;
    letter-spacing: 1px;
    color: var(--ink);
    white-space: nowrap;
  }

  /* Back */
  .name-band {
    position: absolute;
    left: 20px;
    top: 52px;
    width: 295px;
    height: 36px;
    background: var(--band-orange);
  }
  .person-name {
    position: absolute;
    left: 40px;
    top: 52px;
    font-family: "Saira Condensed", "Arial Narrow", sans-serif;
    font-weight: 600;
    font-size: 30px;
    line-height: 1.15;
    color: var(--ink);
    white-space: nowrap;
  }
  .person-role {
    position: absolute;
    left: 40px;
    top: 90px;
    font-family: "Saira Condensed", "Arial Narrow", sans-serif;
    font-weight: 600;
    font-size: 21px;
    line-height: 1.1;
    color: var(--paper-white);
    white-space: nowrap;
  }
  .contact {
    position: absolute;
    left: 40px;
    font-family: "Arimo", Arial, sans-serif;
    font-size: 17px;
    line-height: 1.35;
    color: var(--paper-white);
    white-space: nowrap;
  }
  .contact--address { top: 140px; }
  .contact--reach { top: 206px; }
</style>
</head>
<body>
<main class="canvas">

  <section class="card card--front" aria-label="Business card front">
    <h1 class="brand-name">Tessel PR</h1>
    <div class="tagline-band">
      <p class="tagline">PUBLIC RELATIONS</p>
    </div>
    <svg class="target-ring" viewBox="0 0 150 150" aria-hidden="true">
      <circle cx="75" cy="75" r="71" fill="none" stroke="var(--ink)" stroke-width="4"/>
    </svg>
    <div class="footer-strip" role="img" aria-label="Black and white diagonal warning-stripe band along the card's bottom edge"></div>
  </section>

  <section class="card card--back" aria-label="Business card back">
    <div class="name-band"></div>
    <h2 class="person-name">NADIA WESTBROOK</h2>
    <p class="person-role">MANAGING DIRECTOR</p>
    <p class="contact contact--address">Level 1, 48 Larkin Street,<br>Surry Hills, Sydney 2010</p>
    <p class="contact contact--reach">02 9188 0647<br>nadia@tesselpr.com.au</p>
    <svg class="target-ring" viewBox="0 0 150 150" aria-hidden="true">
      <circle cx="75" cy="75" r="71" fill="none" stroke="var(--ink)" stroke-width="4"/>
    </svg>
    <div class="footer-strip" role="img" aria-label="Black and white diagonal warning-stripe band along the card's bottom edge"></div>
  </section>

</main>
</body>
</html>
```